BRIGHTDESK COWORKING Website design and coding

BRIGHTDESK COWORKING

BRIGHTDESK is Galveston’s first (and currently only) shared business co-working space. We share the same upscale, casual work environment, but we work independently on our own (or our team’s) projects and goals. For only a flat $195 membership fee per month, you have your very own all-inclusive, fun, personal business office environment. Website is written (Word file #12, below); and all pictures etc provided. Galveston is a beachy, coastal, historic city an hour from Houston, Texas USA. Logo (file 11 below) is temporary only.

Target Market(s)

Outside sales people, medical students looking for study hall, Houston companies looking for local office, real estate agents, graphic artists, entrepreneurs, etc

Contact Information for Business Card

will discuss --want to combine with current business card with multiple businesses

Logo Text

BRIGHTDESK COWORKING

Coding

Coded - Design and coding required

Number of Pages Required

5+ page

Colors
ec1f27
fbed22

Requirements
Nice to have
• maroon/wine dominant with yellow and red accents, gray base are the colors of the space--website could coordinate--but open to creative ideas/combinations

```html
<!DOCTYPE html>
<html lang="en">
<head>
<meta charset="utf-8">
<title>Brightdesk Coworking – Contact</title>
<link href="https://fonts.googleapis.com/css2?family=Poppins:wght@400;500;600;700;800;900&display=swap" rel="stylesheet">
<style>
:root{
  --wine:#8a0000;
  --wine-deep:#5e0000;
  --red:#b30e0e;
  --yellow:#fbed22;
  --ink:#1c1f24;
  --white:#ffffff;
  --muted:#d9d9d9;
  --line:#3a3e45;
}
*{margin:0;padding:0;box-sizing:border-box}
html,body{width:1050px;height:1200px;overflow:hidden}
body{font-family:'Poppins',sans-serif;color:var(--white);background:var(--ink);position:relative}
.abs{position:absolute}

.site-header{position:absolute;left:0;top:0;width:1050px;height:60px;background:var(--white)}
.brand{position:absolute;left:78px;top:8px;color:var(--wine);font-weight:800;line-height:1}
.brand .name{font-size:24px;letter-spacing:.5px;display:block}
.brand .sub{font-size:14px;letter-spacing:1px;display:block;margin-left:14px;margin-top:2px}
.nav a{position:absolute;top:24px;font-size:12.5px;color:#222;text-decoration:none;text-transform:uppercase}
.nav a.active{color:var(--wine)}

.hero{position:absolute;left:0;top:60px;width:1050px;height:778px;
  background:radial-gradient(ellipse at 40% 30%,#9a0606 0%,#7a0202 45%,#520000 100%)}

.eyebrow{left:0;width:1050px;top:160px;text-align:center;font-size:27px;font-weight:700}
.headline{left:0;width:1050px;top:193px;text-align:center;font-size:31px;font-weight:900;letter-spacing:.5px}
.lede{left:195px;width:660px;top:238px;text-align:center;font-size:14px;line-height:19px}

.h-sec{font-size:17px;font-weight:700;text-transform:uppercase;line-height:19px}
.info-line{font-size:14px;line-height:20px;display:flex;align-items:center;gap:8px}
.icon{width:12px;height:12px;flex:none}
.block{font-size:14px;line-height:20px}

.social{top:405px;left:154px;display:flex;gap:5px}
.social span{width:28px;height:28px;border-radius:50%;background:rgba(255,255,255,.15);display:block}

.field{position:absolute;left:549px;width:349px;background:var(--white);color:#444;font-size:12px;font-weight:500;padding:0 16px;display:flex;align-items:center}
.field.msg{align-items:flex-start;padding-top:15px}
.submit{position:absolute;left:549px;top:661px;width:349px;height:46px;background:var(--yellow);color:var(--ink);font-weight:700;font-size:17px;display:flex;align-items:center;justify-content:center}

.footer-brand{left:78px;top:990px;color:var(--wine);font-weight:800;line-height:1}
.footer-brand .name{font-size:33px;display:block}
.footer-brand .sub{font-size:20px;display:block;margin-left:22px;margin-top:4px}
.f-h{font-size:14px;font-weight:700;text-transform:uppercase}
.f-row{display:flex;gap:8px;font-size:11.5px;line-height:15.5px;color:var(--muted)}
.f-row .icon{margin-top:2px}
.rule{left:73px;top:1150px;width:904px;height:1px;background:var(--line)}
.copy{left:78px;top:1167px;font-size:12.5px;font-weight:500}
.f-social{top:1168px;left:880px;display:flex;gap:24px}
.f-social span{width:14px;height:14px;border-radius:50%;background:var(--white);display:block}
.to-top{left:986px;top:1133px;width:36px;height:36px;border-radius:50%;background:var(--red);display:flex;align-items:center;justify-content:center}
</style>
</head>
<body>

<header class="site-header">
  <div class="brand"><span class="name">BRIGHTDESK</span><span class="sub">COWORKING</span></div>
  <nav class="nav">
    <a style="left:361px">About</a>
    <a style="left:433px">Amenities</a>
    <a style="left:525px">Membership</a>
    <a style="left:633px">Gallery</a>
    <a style="left:714px">The Brightdesk Philosophy</a>
    <a class="active" style="left:912px">Contact</a>
  </nav>
</header>

<section class="hero" role="img" aria-label="Red-tinted photo of the coworking space interior with desks and lamps"></section>

<h1 class="abs eyebrow">CONTACT US</h1>
<h2 class="abs headline">DESCRIPTION OF YOUR BUSINESS</h2>
<p class="abs lede">Lorem Ipsum is simply dummy text of the printing and typesetting industry. Lorem Ipsum has been the industry's standard dummy text ever since the when an unknown .</p>

<div class="abs" style="left:154px;top:322px">
  <div class="h-sec">Info</div>
  <div class="info-line" style="margin-top:9px">
    <svg class="icon" viewBox="0 0 12 12"><rect x="0" y="2" width="12" height="8" fill="#fbed22"/><path d="M0 2l6 4 6-4" stroke="#8a0000" fill="none"/></svg>
    <span>Email:&nbsp;&nbsp; hello@brightdeskcowork.com</span></div>
  <div class="info-line">
    <svg class="icon" viewBox="0 0 12 12"><path d="M2 1l2.5 0 1 3-1.5 1c.7 1.5 1.8 2.6 3 3l1-1.5 3 1v2.5c-5 .5-9.5-4-9-9z" fill="#fbed22"/></svg>
    <span>Phone:&nbsp; +100 555 0142</span></div>
</div>
<div class="abs social"><span></span><span></span><span></span></div>

<div class="abs" style="left:154px;top:452px">
  <div class="h-sec">Physical Location:</div>
  <div class="block" style="margin-top:2px">Brightdesk Coworking<br>418 Harbor Ave, Suite 12<br>Bayport, TX 77000</div>
  <div class="h-sec" style="margin-top:16px">Owner:</div>
  <div class="block" style="margin-top:3px">Meridian Holdings<br>lee@meridianholds.com<br>555-013-2290</div>
  <div class="h-sec" style="margin-top:14px">Mailing Address for<br>Management:</div>
  <div class="block" style="margin-top:3px">Meridian Holdings<br>77 Commerce Row, Suite 5<br>Rivertown, TX 77001</div>
</div>

<div class="abs h-sec" style="left:546px;top:322px">Contact Form</div>
<div class="field" style="top:352px;height:37px">Name</div>
<div class="field" style="top:396px;height:37px">Email</div>
<div class="field" style="top:440px;height:37px">Phone number</div>
<div class="field" style="top:484px;height:37px">Subject</div>
<div class="field msg" style="top:527px;height:125px">Message</div>
<div class="submit">SUBMIT NOW</div>

<div class="abs footer-brand"><span class="name">BRIGHTDESK</span><span class="sub">COWORKING</span></div>

<div class="abs" style="left:330px;top:946px;width:200px">
  <div class="f-h">Contact Us</div>
  <div class="f-row" style="margin-top:10px">
    <svg class="icon" viewBox="0 0 12 12"><rect x="0" y="2" width="12" height="8" fill="#fbed22"/><path d="M0 2l6 4 6-4" stroke="#1c1f24" fill="none"/></svg>
    <div>Email:<br>hello@brightdeskcowork.com</div></div>
  <div class="f-row" style="margin-top:11px">
    <svg class="icon" viewBox="0 0 12 12"><path d="M2 1l2.5 0 1 3-1.5 1c.7 1.5 1.8 2.6 3 3l1-1.5 3 1v2.5c-5 .5-9.5-4-9-9z" fill="#fbed22"/></svg>
    <div>Phone:<br>555-019-4471</div></div>
</div>

<div class="abs" style="left:567px;top:946px;width:190px">
  <div class="f-h">Physical Location</div>
  <div class="f-row" style="margin-top:9px">
    <svg class="icon" viewBox="0 0 12 12"><path d="M6 0a4 4 0 0 0-4 4c0 3 4 8 4 8s4-5 4-8a4 4 0 0 0-4-4z" fill="#fbed22"/><circle cx="6" cy="4" r="1.5" fill="#1c1f24"/></svg>
    <div>Brightdesk Coworking<br>418 Harbor Ave, Suite 12<br>Bayport, TX 77000</div></div>
</div>

<div class="abs" style="left:764px;top:946px;width:220px">
  <div class="f-h">Owner</div>
  <div class="f-row" style="margin-top:9px;color:#fff">Meridian Holdings</div>
  <div class="f-row" style="margin-top:10px">
    <svg class="icon" viewBox="0 0 12 12"><rect x="0" y="2" width="12" height="8" fill="#fbed22"/><path d="M0 2l6 4 6-4" stroke="#1c1f24" fill="none"/></svg>
    <div>lee@meridianholds.com</div></div>
  <div class="f-row" style="margin-top:7px">
    <svg class="icon" viewBox="0 0 12 12"><path d="M2 1l2.5 0 1 3-1.5 1c.7 1.5 1.8 2.6 3 3l1-1.5 3 1v2.5c-5 .5-9.5-4-9-9z" fill="#fbed22"/></svg>
    <div>555-013-2290</div></div>
  <div class="f-row" style="margin-top:7px">
    <svg class="icon" viewBox="0 0 12 12"><path d="M6 0a4 4 0 0 0-4 4c0 3 4 8 4 8s4-5 4-8a4 4 0 0 0-4-4z" fill="#fbed22"/><circle cx="6" cy="4" r="1.5" fill="#1c1f24"/></svg>
    <div>Meridian Holdings<br>77 Commerce Row, Suite 5<br>Rivertown, TX 77001</div></div>
</div>

<div class="abs rule"></div>
<div class="abs copy">Copyright © 2020, Brightdesk Coworking. All Rights Reserved</div>
<div class="abs f-social"><span></span><span></span><span></span></div>
<div class="abs to-top"><svg width="12" height="12" viewBox="0 0 12 12"><path d="M6 11V1M2 5l4-4 4 4" stroke="#fff" stroke-width="1.3" fill="none"/></svg></div>

</body>
</html>
```